Redesign of Engineering firm website

I want a redesign of the velkorpower.com website with the below in mind:

1- the client has a 3 main sectors: Renewable Energy, Process Automation and General Engineering.
2- Home page should show the 3 sectors
3- the other standard pages should be home, About, Clients, Projects, Training, Career, and Contact
4- The theme should be wordpress.
5- Responsive layout that works with all devices
6- One page layout is preferable for the home page.
7- it should be original and is not copied from other templates.

Target Market(s)

Engineers and professional

Industry/Entity Type

Solar Energy

Font styles to use
Serif
Sans Serif

Colors
3277b5
0355a3
0493ce

Requirements
Must have
• pictures that represent the three sectors

```html
<!DOCTYPE html>
<html lang="en">
<head>
<meta charset="utf-8">
<title>Velkor Power – Solar Engineering</title>
<link href="https://fonts.googleapis.com/css2?family=Raleway:wght@300;400;500;600;700;800&family=Open+Sans:wght@400;600;700&display=swap" rel="stylesheet">
<style>
:root{
  --blue:#0b8db0;
  --blue-dark:#0577a0;
  --blue-brand:#0493ce;
  --yellow:#f6c22b;
  --ink:#333;
  --muted:#666;
  --light:#eef3f6;
  --dark:#2e3032;
  --white:#fff;
}
*{box-sizing:border-box;margin:0;padding:0}
html,body{width:1200px;height:4245px;overflow:hidden;background:var(--white)}
body{font-family:"Open Sans",Arial,sans-serif;color:var(--ink)}
.page{position:relative;width:1200px;height:4245px;overflow:hidden}
.abs{position:absolute}
.bg-layer{position:absolute;left:0;top:0}
.heading{font-family:"Raleway",Arial,sans-serif;font-weight:400;font-size:46px;color:var(--ink);text-align:center;width:1200px;left:0}
.heading b{font-weight:700;color:var(--blue)}
.heading.on-dark{color:var(--white)}
.heading-rule{position:absolute;height:4px;width:120px;left:540px;background:repeating-linear-gradient(90deg,var(--yellow) 0 8px,transparent 8px 11px)}
.btn-more{position:absolute;height:30px;border-radius:15px;background:var(--yellow);font:600 13px "Open Sans",sans-serif;color:var(--ink);padding:0 44px 0 16px;line-height:30px}
.btn-more::after{content:"»";position:absolute;right:3px;top:3px;width:24px;height:24px;border-radius:12px;background:var(--ink);color:var(--white);text-align:center;line-height:22px;font-size:15px}

/* header */
.topbar{left:690px;top:0;width:510px;height:34px;background:var(--blue)}
.topbar-call{left:712px;top:8px;font-size:14px;color:var(--white);white-space:nowrap}
.social{position:absolute;top:7px;width:20px;height:20px;border-radius:50%;background:var(--white);opacity:.9}
.logo{left:165px;top:30px;font:800 52px "Raleway",sans-serif;color:var(--blue-brand);letter-spacing:1px}
.nav{left:440px;top:60px;display:flex}
.nav a{font:400 14px "Raleway",sans-serif;color:var(--ink);text-decoration:none;padding:8px 16px;margin-right:24px}
.nav a.active{color:var(--blue);border-left:1px solid #ddd;border-right:1px solid #ddd;border-bottom:3px solid var(--blue)}

/* hero */
.hero-photo{left:0;top:120px;width:1200px;height:480px;background:linear-gradient(180deg,#4f80b2 0%,#5b8cbe 30%,#3f6e9f 55%,#2f5d8f 66%,#5f8f2e 80%,#4d7a25 100%)}
.hero-title{right:162px;top:298px;width:520px;text-align:right;font:500 36px/42px "Raleway",sans-serif;color:var(--white);text-shadow:0 2px 6px rgba(0,0,0,.55)}

/* about */
.island{left:113px;top:622px;width:440px;height:326px;border-radius:48% 52% 40% 40%;background:radial-gradient(circle at 50% 35%,#7fd36b 0%,#4aa55b 40%,#3c9fb8 70%,rgba(60,159,184,0) 72%)}
.about-title{left:640px;top:642px;font:400 42px/46px "Raleway",sans-serif;color:var(--white)}
.about-title b{display:block;font-weight:800;font-size:50px}
.about-text{left:640px;top:758px;width:410px;font-size:13.5px;line-height:19px;color:var(--white)}
.globe{left:736px;top:1132px;width:354px;height:298px;border-radius:50%;background:radial-gradient(circle at 50% 40%,#8dd46b 0%,#4ea84d 50%,#2f7e3c 75%)}
.pillar{position:absolute;left:164px;width:420px}
.pillar-icon{position:absolute;left:0;top:0;width:58px;height:58px;border-radius:6px}
.pillar h3{position:absolute;left:82px;top:-6px;font:400 28px "Raleway",sans-serif;color:var(--white)}
.pillar p{position:absolute;left:82px;top:38px;width:330px;font-size:13px;line-height:18px;color:var(--white)}

/* services */
.services-intro{left:180px;top:1676px;width:840px;text-align:center;font-size:13px;line-height:19px;color:#e6e6e6}
.service h4{font:600 18px "Raleway",sans-serif;color:var(--blue-brand)}
.service p{font-size:12.5px;line-height:17px;color:#e6e6e6;margin-top:4px}
.service-icon{position:absolute;width:66px;height:66px;border-radius:50%}
.sun{left:450px;top:1920px;width:300px;height:300px;border-radius:50%;background:radial-gradient(circle at 45% 40%,#ffe066 0%,#f4b41a 100%)}
.sun-name{left:450px;top:2036px;width:300px;text-align:center;font:800 54px "Raleway",sans-serif;color:#4a4a4a}

/* projects */
.card{position:absolute;top:2366px;width:272px;height:318px;background:var(--white);box-shadow:0 2px 10px rgba(0,0,0,.14)}
.card-photo{height:160px;background:linear-gradient(180deg,#9fc3e6 0%,#cfe0ef 35%,#2d5f9a 55%,#234a7a 100%)}
.card h5{text-align:center;font:700 17px "Open Sans",sans-serif;color:var(--blue);margin-top:18px}
.card p{text-align:center;font-size:12px;line-height:17px;color:var(--muted);padding:6px 22px 0}
.card-sun{position:absolute;left:124px;bottom:10px;width:24px;height:12px;border-radius:12px 12px 0 0;background:var(--yellow)}
.arrow{position:absolute;font:300 48px "Raleway",sans-serif;color:#555}

/* testimonial */
.person{left:140px;top:2730px;width:255px;height:510px;background:linear-gradient(180deg,#d9c4a8 0%,#2e2e33 35%,#2e2e33 65%,#3f5f86 100%);border-radius:80px 80px 0 0}
.quote{left:461px;top:2956px;width:580px;font-style:italic;font-size:13.5px;line-height:20px;color:var(--white)}
.quote-by{left:461px;top:3094px;font-size:13px;font-weight:700;color:var(--white)}
.dot{position:absolute;top:3142px;width:10px;height:10px;border-radius:50%;border:2px solid var(--white)}

/* clients */
.client{position:absolute;top:3433px;width:132px;height:86px;border:1px solid #e2e2e2;background:#f7f7f7;display:flex;align-items:center;justify-content:center;font:600 18px "Raleway",sans-serif;color:#777}

/* contact */
.contact-title{left:161px;top:3660px;font:400 48px "Raleway",sans-serif;color:var(--white)}
.contact-title b{color:var(--blue-brand);font-weight:700}
.contact-lead{left:161px;top:3776px;font-size:14px;color:#ddd}
.col-head{position:absolute;top:3850px;font:600 16px "Raleway",sans-serif;color:var(--white)}
.field{position:absolute;left:161px;width:255px;background:#222;border:1px solid #444;color:#888;font-size:11px;padding:6px 8px}
.send{left:161px;top:4050px;width:84px;height:26px;background:#ddd;font:700 12px "Open Sans",sans-serif;color:#333;text-align:center;line-height:26px}
.map{left:470px;top:3891px;width:255px;height:150px;background:linear-gradient(135deg,#e6e6e2,#d4d8d0)}
.find{position:absolute;left:818px;font-size:12.5px;line-height:18px;color:#ddd}
.find-icon{position:absolute;left:790px;width:14px;height:14px}
.sq{position:absolute;top:4024px;width:22px;height:22px;background:#bbb}

/* newsletter & footer */
.newsletter{left:0;top:4112px;width:1200px;height:91px;background:var(--yellow)}
.news-label{left:221px;top:4142px;font:400 24px "Raleway",sans-serif;color:var(--ink)}
.news-input{left:518px;top:4143px;width:317px;height:32px;background:var(--white);font-size:12px;color:#777;padding:8px 10px}
.news-btn{left:843px;top:4143px;width:167px;height:32px;background:var(--blue-brand);color:var(--white);font:700 14px "Open Sans",sans-serif;text-align:center;line-height:32px;letter-spacing:1px}
.footer{left:0;top:4203px;width:1200px;height:42px;background:#1f1f1f;color:#aaa;font-size:11px;text-align:center;line-height:42px}
</style>
</head>
<body>
<div class="page">

  <svg class="bg-layer" width="1200" height="4245" viewBox="0 0 1200 4245" aria-hidden="true">
    <rect x="0" y="600" width="1200" height="1000" fill="var(--light)"/>
    <polygon points="600,600 1200,600 1200,990 600,1118" fill="var(--blue)"/>
    <polygon points="0,1033 600,1118 600,1490 0,1580" fill="var(--blue)"/>
    <defs>
      <linearGradient id="darkGrad" x1="0" y1="0" x2="1" y2="1">
        <stop offset="0" stop-color="#3d3f42"/><stop offset="1" stop-color="#232527"/>
      </linearGradient>
    </defs>
    <polygon points="0,1580 600,1490 1200,1405 1200,2210 0,2100" fill="url(#darkGrad)"/>
    <polygon points="0,2830 1200,2740 1200,3295 0,3225" fill="var(--blue)"/>
    <polygon points="0,3588 1200,3650 1200,4112 0,4112" fill="var(--dark)"/>
  </svg>

  <!-- header -->
  <div class="abs topbar"></div>
  <div class="abs topbar-call">Call Us Now: 123 456 7890</div>
  <span class="social" style="left:930px"></span>
  <span class="social" style="left:956px"></span>
  <span class="social" style="left:982px"></span>
  <span class="social" style="left:1008px"></span>
  <div class="abs logo">VELKOR</div>
  <nav class="abs nav">
    <a class="active">Home</a><a>About Us</a><a>Services</a><a>Training</a><a>Employment</a><a>Contact Us</a>
  </nav>

  <!-- hero -->
  <div class="abs hero-photo" role="img" aria-label="Photo of two engineers in hard hats reviewing plans in front of a solar panel field"></div>
  <h1 class="abs hero-title">Velkor scope goes beyond engineering, procurement and construction.</h1>
  <div class="btn-more" style="left:910px;top:452px">Read More</div>

  <!-- about -->
  <div class="abs island" role="img" aria-label="Illustration of a floating island with wind turbines, solar panels and a house"></div>
  <h2 class="abs about-title">About <b>VELKOR</b></h2>
  <p class="abs about-text">We are the solar experts in the solar kingdom. The KSA (Saudi Arabia) solar market is a promising market with huge potential. The plan is to build 41,000 MW of solar in the coming 20 years, as announced by S.E.R.A. (Solar Energy Resource Authority). We provide our services, both by our in-house team and associated partners. All together have diversified expertise covering various aspects of solar PV.</p>
  <div class="btn-more" style="left:645px;top:931px">Read More</div>

  <div class="pillar" style="top:1166px">
    <svg class="pillar-icon" viewBox="0 0 58 58" aria-hidden="true"><rect width="58" height="58" rx="6" fill="#1a9fc2"/><circle cx="29" cy="29" r="15" fill="none" stroke="#fff" stroke-width="3"/><circle cx="29" cy="29" r="7" fill="none" stroke="#fff" stroke-width="3"/><circle cx="29" cy="29" r="2" fill="#fff"/></svg>
    <h3>Our Mission</h3>
    <p>To contribute to the GCC transformative change to the solar industry with focus on the connection between people, place, and technology.</p>
  </div>
  <div class="pillar" style="top:1316px">
    <svg class="pillar-icon" viewBox="0 0 58 58" aria-hidden="true"><rect width="58" height="58" rx="6" fill="#1a9fc2"/><path d="M10 29 Q29 12 48 29 Q29 46 10 29Z" fill="none" stroke="#fff" stroke-width="3"/><circle cx="29" cy="29" r="6" fill="#fff"/></svg>
    <h3>Our Vision</h3>
    <p>To become the GCC hub for solar knowledge and business creation (including photovoltaics (PV), CPV, concentrating solar power CSP and solar thermal technologies).</p>
  </div>
  <div class="abs globe" role="img" aria-label="Illustration of a half globe with green hills, houses and wind turbines"></div>

  <!-- services -->
  <h2 class="abs heading on-dark" style="top:1598px">Our <b>Services</b></h2>
  <div class="heading-rule" style="top:1662px"></div>
  <p class="abs services-intro">Velkor-Solar: provides Solar Energy consulting services, Energy Efficiency Consulting services and Data Collection function. With services spanning the entire project lifecycle, Velkor scope goes beyond engineering, procurement and construction.</p>

  <div class="abs service" style="left:400px;top:1740px;width:400px;text-align:center">
    <h4>General Engineering</h4>
    <p>Duis aute irure dolor in reprehenderit in voluptate velit esse cillum dolore eu fugiat nulla pariatur.</p>
  </div>
  <div class="abs service" style="left:150px;top:1918px;width:220px">
    <h4>Renewable Energy</h4>
    <p>Duis aute irure dolor in reprehenderit in voluptate velit esse cillum dolore eu fugiat nulla pariatur.</p>
  </div>
  <div class="abs service" style="left:830px;top:1918px;width:220px">
    <h4>Process Automation</h4>
    <p>Duis aute irure dolor in reprehenderit in voluptate velit esse cillum dolore eu fugiat nulla pariatur.</p>
  </div>

  <svg class="service-icon" style="left:567px;top:1810px" viewBox="0 0 66 66" aria-hidden="true"><circle cx="33" cy="33" r="33" fill="#fff"/><path d="M19 38 Q19 22 33 22 Q47 22 47 38Z" fill="#333"/><rect x="16" y="38" width="34" height="5" rx="2" fill="#333"/></svg>
  <svg class="service-icon" style="left:377px;top:1923px" viewBox="0 0 66 66" aria-hidden="true"><circle cx="33" cy="33" r="33" fill="#fff"/><rect x="24" y="26" width="18" height="16" rx="3" fill="#333"/><rect x="27" y="18" width="3" height="9" fill="#333"/><rect x="36" y="18" width="3" height="9" fill="#333"/><rect x="31" y="42" width="4" height="8" fill="#333"/></svg>
  <svg class="service-icon" style="left:754px;top:1923px" viewBox="0 0 66 66" aria-hidden="true"><circle cx="33" cy="33" r="33" fill="#fff"/><path d="M16 33 L33 18 L50 33" fill="none" stroke="#333" stroke-width="4"/><path d="M21 31 V48 H45 V31" fill="none" stroke="#333" stroke-width="4"/><circle cx="33" cy="39" r="4" fill="#333"/></svg>

  <div class="abs sun" role="img" aria-label="Illustration of a bright yellow sun with rays"></div>
  <div class="abs sun-name">VELKOR</div>

  <!-- projects -->
  <h2 class="abs heading" style="top:2256px">Latest <b>Projects</b></h2>
  <div class="heading-rule" style="top:2318px"></div>
  <span class="arrow" style="left:124px;top:2490px">‹</span>
  <span class="arrow" style="left:1052px;top:2490px">›</span>

  <article class="card" style="left:164px">
    <div class="card-photo" role="img" aria-label="Photo of a row of solar panels under a blue sky"></div>
    <h5>Duis aute irure dolor</h5>
    <p>Duis aute irure dolor in reprehenderit in voluptate velit esse cillum dolore eu fugiat nulla pariatur. Duis aute irure dolor in reprehenderit in voluptate</p>
    <span class="card-sun"></span>
  </article>
  <article class="card" style="left:464px">
    <div class="card-photo" role="img" aria-label="Photo of a solar farm with wind turbines behind" style="background:linear-gradient(180deg,#b8d3ea 0%,#e2ecf4 40%,#3a6aa3 60%,#2c5584 100%)"></div>
    <h5>Duis aute irure dolor</h5>
    <p>Duis aute irure dolor in reprehenderit in voluptate velit esse cillum dolore eu fugiat nulla pariatur. Duis aute irure dolor in reprehenderit in voluptate</p>
    <span class="card-sun"></span>
  </article>
  <article class="card" style="left:764px">
    <div class="card-photo" role="img" aria-label="Photo of technicians installing solar panels on a red roof" style="background:linear-gradient(160deg,#b4432f 0%,#8e2f24 45%,#3b4a63 70%,#2a3346 100%)"></div>
    <h5>Duis aute irure dolor</h5>
    <p>Duis aute irure dolor in reprehenderit in voluptate velit esse cillum dolore eu fugiat nulla pariatur. Duis aute irure dolor in reprehenderit in voluptate</p>
    <span class="card-sun"></span>
  </article>

  <!-- testimonial -->
  <div class="abs person" role="img" aria-label="Photo of a smiling man in a dark t-shirt giving a thumbs up"></div>
  <h2 class="abs" style="left:453px;top:2860px;font:400 46px 'Raleway',sans-serif;color:#1d3f4d">What <b style="font-weight:700;color:var(--white)">People Say?</b></h2>
  <p class="abs quote">“Lorem ipsum dolor sit amet, consectetuer adipiscing elitnk, sed amet diam nonummy nibh euismod tincidun nit utem laoreetnd dolore magna aliquam erat volutpat. Ut wisi enim ad minim veniam, quis nostrud exer tationk ullamcorb per suscipit lobortisk nisl utnd aliqui ex ea commodo consequat. Duis autem vel eumk iriure dolor inji hendrerit inn vulputate velit esse mk molestaimo consequat, velhlo illuem geal dolore eu feugiat nulla facilisis.</p>
  <div class="abs quote-by">- Rana Idris</div>
  <span class="dot" style="left:461px;background:var(--white)"></span>
  <span class="dot" style="left:477px"></span>
  <span class="dot" style="left:493px"></span>

  <!-- clients -->
  <h2 class="abs heading" style="top:3302px">Our <b>Clients</b></h2>
  <div class="heading-rule" style="top:3364px"></div>
  <span class="arrow" style="left:112px;top:3448px;color:#bbb">‹</span>
  <span class="arrow" style="left:1066px;top:3448px;color:#bbb">›</span>
  <div class="client" style="left:161px">Halvern</div>
  <div class="client" style="left:313px">NORTEX</div>
  <div class="client" style="left:465px">KORA</div>
  <div class="client" style="left:617px">Veltris</div>
  <div class="client" style="left:769px">Brightmoor</div>
  <div class="client" style="left:921px">Stanlow</div>

  <!-- contact -->
  <h2 class="abs contact-title">Contact <b>Us</b></h2>
  <div class="heading-rule" style="top:3730px;left:161px"></div>
  <p class="abs contact-lead">Come on by! We'd love to see you</p>

  <div class="col-head" style="left:161px">Drop us a line</div>
  <div class="field" style="top:3886px;height:28px">Name</div>
  <div class="field" style="top:3920px;height:28px">Email</div>
  <div class="field" style="top:3954px;height:88px">Message</div>
  <div class="abs send">SEND</div>

  <div class="col-head" style="left:470px">Location Map</div>
  <div class="abs map" role="img" aria-label="Street map showing the office location with a red pin"></div>

  <div class="col-head" style="left:790px">Find Us</div>
  <svg class="find-icon" style="top:3893px" viewBox="0 0 14 14" aria-hidden="true"><path d="M7 1 C4 1 2.5 3.2 2.5 5.3 C2.5 8.5 7 13 7 13 S11.5 8.5 11.5 5.3 C11.5 3.2 10 1 7 1Z" fill="#ddd"/><circle cx="7" cy="5.3" r="1.8" fill="#2e3032"/></svg>
  <p class="find" style="top:3889px"><b style="color:var(--white)">VELKOR</b><br>Al-Khobar - Tower 14 - Eastern Province 31000<br>Kingdom of Saudi Arabia</p>
  <svg class="find-icon" style="top:3964px" viewBox="0 0 14 14" aria-hidden="true"><path d="M3 1 L5.5 1 L6.5 4 L5 5.2 Q6.3 8 8.8 9 L10 7.5 L13 8.5 L13 11 Q12.5 13 10.5 13 Q1 11 1 3 Q1 1 3 1Z" fill="#ddd"/></svg>
  <p class="find" style="top:3961px">+966 13 555 0147</p>
  <svg class="find-icon" style="top:3995px" viewBox="0 0 14 14" aria-hidden="true"><rect x="1" y="3" width="12" height="8" fill="#ddd"/><path d="M1 3 L7 8 L13 3" fill="none" stroke="#2e3032" stroke-width="1.2"/></svg>
  <p class="find" style="top:3992px">info@velkorpower.com</p>
  <span class="sq" style="left:790px"></span>
  <span class="sq" style="left:818px"></span>
  <span class="sq" style="left:846px"></span>
  <span class="sq" style="left:874px"></span>

  <!-- newsletter -->
  <div class="abs newsletter"></div>
  <svg class="abs" style="left:166px;top:4141px" width="36" height="36" viewBox="0 0 36 36" aria-hidden="true"><circle cx="18" cy="18" r="16" fill="none" stroke="#333" stroke-width="2"/><rect x="9" y="12" width="18" height="12" fill="none" stroke="#333" stroke-width="2"/><path d="M9 12 L18 19 L27 12" fill="none" stroke="#333" stroke-width="2"/></svg>
  <div class="abs news-label">Sign Up For Newsletter</div>
  <div class="abs news-input">Enter your email here</div>
  <div class="abs news-btn">SUBSCRIBE</div>

  <footer class="abs footer">Copyright © 2017 VELKOR. All Right Reserved</footer>
</div>
</body>
</html>
```